Marmot Harbor concert poster 0918

Marmot Harbor is a 1990's alternative rock cover band in the Philadelphia area. We need a poster design for an upcoming gig. See 'Must Haves' for key elements.
Our set includes songs by Glumbo, RVK, Tin Drifters, Calyxo, Colder than Moss, Paravent, Rust Hour, Vox, Sixth Lamp Quiet, Rye Pockets, etc. If you know this music, you'll get it. Our set is high energy and upbeat, and we don't take ourselves too seriously.
Style: I leave that to you, but I like many of the recent concert posters done for Kolvat, if that's any indication of what I'm looking for. Maybe a subtle 1990s reference, or something to convey the 1990s style or music.
You can find our current logo on www.friendwall.example/brindle88s - you may choose to work with this, or not, your option. The award will be based on my subjective overall impression. If you choose to include a new logo design on the poster, we may use it for ongoing projects (T-shirts, etc).

Target Market(s)

Music-minded people from ages 21-55, with sweet spot around the age 40s. The poster will hang in restaurants and shops in suburbia, so images should be chosen accordingly.

Font styles to use
Sans Serif

Colors

Designer to choose colors to be used in the design.

Requirements
Must have
• Highly legible (from 5 meters or so away) - will hang in suburban restaurants and store windows.
• Sized to print 11"x17" poster format
• Date and time of event (Sept 29, 9pm), and venue (Harlow Alehouse, Jenkintown).
• A reference to "'90s alt rock" or "'90s alternative rock" is also important.
• Visual interest, and ability for this to serve as a template for future events (by changing the date and venue name)
Nice to have
• Bold color
• A '90's rock feel
• Ok to use our logo art attached, not required
Should not have
• Images that don't fit a restaurant setting (like a live or dead opossum, which looks like a rat)
• Too busy / tough to read
• Monochrome / greyscale

```html
<!DOCTYPE html>
<html lang="en">
<head>
<meta charset="utf-8">
<title>Marmot Harbor – 90s Alternative Rock</title>
<link rel="stylesheet" href="https://fonts.googleapis.com/css2?family=Alfa+Slab+One&family=Rye&family=Rubik+Wet+Paint&display=swap">
<style>
  :root {
    --page: #ffffff;
    --paper-light: #f1e6c4;
    --paper: #e6d39f;
    --paper-edge: #cfb270;
    --frame: #6a2a14;
    --rust: #5f2210;
    --ink: #111111;
    --white: #ffffff;
    --mascot-tone: #9a9384;
  }
  * { margin: 0; padding: 0; box-sizing: border-box; }
  html, body {
    width: 777px; height: 1200px; overflow: hidden; background: var(--page);
  }
  .poster { position: relative; width: 777px; height: 1200px; }
  .paper { position: absolute; inset: 0; }
  .frame {
    position: absolute; left: 65px; top: 73px; width: 643px; height: 1039px;
    border: 2px solid var(--frame);
  }
  .band-name {
    position: absolute; left: 0; right: 0; top: 150px; text-align: center;
    font-family: "Alfa Slab One", serif; font-size: 54px; color: var(--ink);
    letter-spacing: 1px;
  }
  .mascot {
    position: absolute; left: 318px; top: 305px; width: 135px; height: 86px;
    background: radial-gradient(ellipse at center, var(--mascot-tone) 0%, rgba(154,147,132,0.25) 70%, transparent 100%);
    border-radius: 40%;
  }
  .guitars {
    position: absolute; left: 96px; top: 351px; width: 590px; height: 510px;
    background: radial-gradient(ellipse at 50% 58%, rgba(255,255,255,0.85) 0%, rgba(255,255,255,0.55) 45%, rgba(255,255,255,0) 72%);
  }
  .genre {
    position: absolute; left: 0; right: 0; text-align: center;
    font-family: "Rubik Wet Paint", sans-serif; color: var(--rust);
    line-height: 1;
  }
  .genre-decade { top: 455px; font-size: 168px; }
  .genre-style { top: 648px; font-size: 56px; letter-spacing: -1px; }
  .genre-word { top: 712px; font-size: 138px; }
  .date {
    position: absolute; left: 0; right: 0; top: 898px; text-align: center;
    font-family: "Alfa Slab One", serif; font-size: 42px; color: var(--ink);
    letter-spacing: 2px;
  }
  .divider {
    position: absolute; left: 215px; top: 973px; width: 357px; height: 3px;
    background: var(--ink);
  }
  .venue {
    position: absolute; left: 0; right: 0; top: 1003px; text-align: center;
    font-family: "Rye", serif; font-size: 30px; line-height: 42px;
    color: var(--frame);
  }
</style>
</head>
<body>
<main class="poster">
  <svg class="paper" width="777" height="1200" viewBox="0 0 777 1200" aria-hidden="true">
    <defs>
      <radialGradient id="paperTone" cx="50%" cy="50%" r="70%">
        <stop offset="0%" stop-color="var(--paper-light)"/>
        <stop offset="70%" stop-color="var(--paper)"/>
        <stop offset="100%" stop-color="var(--paper-edge)"/>
      </radialGradient>
    </defs>
    <polygon fill="url(#paperTone)" points="
      26,34 60,30 95,36 130,29 170,35 210,30 250,37 290,31 330,36 370,29 410,35 450,30 490,37 530,31 570,36 610,29 650,35 690,30 725,37 752,32
      747,70 753,110 746,150 752,190 745,230 751,270 746,310 753,350 745,390 751,430 746,470 752,510 745,550 751,590 746,630 753,670 745,710 751,750 746,790 752,830 745,870 751,910 746,950 753,990 745,1030 751,1070 746,1110 752,1150 748,1176
      710,1170 670,1177 630,1171 590,1178 550,1170 510,1176 470,1171 430,1178 390,1170 350,1177 310,1171 270,1178 230,1170 190,1176 150,1171 110,1178 70,1170 28,1175
      33,1140 26,1100 32,1060 25,1020 31,980 26,940 33,900 25,860 31,820 26,780 32,740 25,700 31,660 26,620 33,580 25,540 31,500 26,460 32,420 25,380 31,340 26,300 33,260 25,220 31,180 26,140 32,100 25,66"/>
  </svg>
  <div class="frame"></div>

  <h1 class="band-name">MARMOT HARBOR</h1>
  <div class="mascot" role="img" aria-label="Band mascot illustration wearing a small crown"></div>
  <div class="guitars" role="img" aria-label="Two crossed white electric guitars behind the headline"></div>

  <div class="genre genre-decade">90S</div>
  <div class="genre genre-style">ALTERNATIVE</div>
  <div class="genre genre-word">ROCK</div>

  <p class="date">SEPT 29, 9:00 PM</p>
  <div class="divider"></div>
  <p class="venue">HARLOW ALEHOUSE,<br>JENKINTOWN</p>
</main>
</body>
</html>
```